Real Estate Business Cards

Looking for a clean, sharp and professional look for our Real Estate investment Fund that invests in Multi Family Apartment buildings.

Target Market(s)

Real Estate Fund

Industry/Entity Type

Real Estate

Contact Information for Business Card

Company Description: Real Estate Investment Fund
Company Name: RKW Holdings
Name: Marcus Olvane
Cell: (917) 482-0657
Email: marcus@rkwholdings-example.com
Website: www.rkwholdings-example.com
Address: 418, 9th Street, Brooklyn NY 11218

Colors

Designer to choose colors to be used in the design.

Requirements
Nice to have
• Colors to match logo

```html
<!DOCTYPE html>
<html lang="en">
<head>
<meta charset="utf-8">
<title>RKW Holdings – Business Cards</title>
<link rel="stylesheet" href="https://fonts.googleapis.com/css2?family=Marcellus&family=Roboto:wght@400&family=Montserrat:wght@400&display=swap">
<style>
  :root {
    --brand-blue: #1170aa;
    --ink-blue: #1a6ea8;
    --ink-grey: #4a4a4a;
    --divider: #3d3d3d;
    --paper: #ffffff;
    --backdrop: #eeeeee;
  }
  * { margin: 0; padding: 0; box-sizing: border-box; }
  html, body { width: 1200px; height: 800px; overflow: hidden; background: var(--backdrop); }
  .canvas { position: relative; width: 1200px; height: 800px; }

  .card { position: absolute; width: 571px; height: 328px; box-shadow: 0 6px 18px rgba(0,0,0,0.12); }
  .card--front { left: 475px; top: 32px; background: var(--paper); }
  .card--back { left: 170px; top: 406px; background: var(--brand-blue); }

  /* Front card */
  .front-brand { position: absolute; left: 56px; top: 104px; width: 220px; text-align: center; }
  .front-brand__square { width: 52px; height: 52px; background: var(--brand-blue); margin: 0 auto 22px; }
  .front-brand__name {
    font-family: "Marcellus", serif; font-size: 23px; color: var(--ink-blue);
    text-transform: uppercase; letter-spacing: 0.5px; white-space: nowrap;
  }
  .front-divider { position: absolute; left: 284px; top: 100px; width: 2px; height: 129px; background: var(--divider); }

  .person { position: absolute; left: 302px; top: 97px; }
  .person__name {
    font-family: "Marcellus", serif; font-size: 21px; color: var(--ink-blue);
    text-transform: uppercase; letter-spacing: 0.3px; line-height: 1;
  }
  .person__title { font-family: "Roboto", sans-serif; font-size: 16px; color: var(--ink-grey); margin-top: 6px; }

  .contact-list { position: absolute; left: 302px; top: 168px; list-style: none; }
  .contact-list li {
    display: flex; align-items: center; gap: 5px; height: 22px;
    font-family: "Roboto", sans-serif; font-size: 15.5px; color: var(--ink-grey); white-space: nowrap;
  }
  .contact-list svg { width: 12px; height: 12px; fill: var(--ink-blue); flex: none; }

  .address {
    position: absolute; left: 0; right: 0; top: 265px; text-align: center;
    font-family: "Roboto", sans-serif; font-size: 16px; color: var(--ink-grey);
    display: flex; justify-content: center; align-items: center; gap: 5px;
  }
  .address svg { width: 12px; height: 15px; fill: var(--ink-blue); }

  /* Back card */
  .back-brand { position: absolute; left: 85px; top: 108px; display: flex; align-items: center; gap: 28px; }
  .back-brand__square { width: 100px; height: 100px; border: 5px solid var(--paper); }
  .back-brand__name {
    font-family: "Marcellus", serif; font-size: 34px; color: var(--paper);
    text-transform: uppercase; letter-spacing: 1px; white-space: nowrap;
  }
  .tagline {
    position: absolute; left: 0; right: 0; top: 271px; text-align: center;
    font-family: "Montserrat", sans-serif; font-size: 15px; color: var(--paper); letter-spacing: 1.2px;
  }
</style>
</head>
<body>
<main class="canvas">

  <section class="card card--front" aria-label="Business card front">
    <div class="front-brand">
      <div class="front-brand__square"></div>
      <div class="front-brand__name">RKW Holdings</div>
    </div>
    <div class="front-divider"></div>

    <div class="person">
      <h1 class="person__name">Marcus Olvane</h1>
      <p class="person__title">Managing Director</p>
    </div>

    <ul class="contact-list">
      <li>
        <svg viewBox="0 0 24 24" aria-hidden="true"><path d="M6.6 10.8c1.4 2.8 3.8 5.1 6.6 6.6l2.2-2.2c.3-.3.7-.4 1-.2 1.1.4 2.3.6 3.6.6.6 0 1 .4 1 1V20c0 .6-.4 1-1 1C10.6 21 3 13.4 3 4c0-.6.4-1 1-1h3.5c.6 0 1 .4 1 1 0 1.3.2 2.5.6 3.6.1.3 0 .7-.2 1z"/></svg>
        (917) 482-0657
      </li>
      <li>
        <svg viewBox="0 0 24 24" aria-hidden="true"><path d="M2 5h20v14H2z M2 5l10 8 10-8" fill="none" stroke="#1a6ea8" stroke-width="0"/><path d="M2 6.5V19h20V6.5l-10 7.5z M2.5 5h19L12 12.2z"/></svg>
        marcus@rkwholdings-example.com
      </li>
      <li>
        <svg viewBox="0 0 24 24" aria-hidden="true"><circle cx="12" cy="12" r="10"/><path d="M2 12h20M12 2c3 3 3 17 0 20M12 2c-3 3-3 17 0 20" stroke="#fff" stroke-width="1.5" fill="none"/></svg>
        www.rkwholdings-example.com
      </li>
    </ul>

    <p class="address">
      <svg viewBox="0 0 20 26" aria-hidden="true"><path d="M10 0C4.5 0 0 4.4 0 9.8 0 17 10 26 10 26s10-9 10-16.2C20 4.4 15.5 0 10 0zm0 13.5a3.7 3.7 0 1 1 0-7.4 3.7 3.7 0 0 1 0 7.4z"/></svg>
      418, 9th Street, Brooklyn NY 11218
    </p>
  </section>

  <section class="card card--back" aria-label="Business card back">
    <div class="back-brand">
      <div class="back-brand__square"></div>
      <div class="back-brand__name">RKW Holdings</div>
    </div>
    <p class="tagline">Real Estate Investment Fund</p>
  </section>

</main>
</body>
</html>
```